Brightmoor Vector Systems Website

I am starting an IT consulting business called Brightmoor Vector Systems. I recently completed a logo contest on ArtHive and am now looking to put together a basic website. I can provide text and content but am looking for a site design with layout and graphics. I am attaching my logo below. I was thinking of a dark blue and white theme for the website (similar to the logo). However, I am open to ideas. Graphics can be a mix of business and high tech as that is the image I am trying to convey. The site will be relatively simple and probably have only 3 - 5 pages (Home, About Us, Services, Contact, etc.)
Target Market(s)
United States commercial companies and government contractors
Industry/Entity Type
Consulting

```html
<!DOCTYPE html>
<html lang="en">
<head>
<meta charset="utf-8">
<title>Brightmoor Vector Systems</title>
<link rel="stylesheet" href="https://fonts.googleapis.com/css2?family=Bebas+Neue&family=Raleway:wght@500;700;800&family=Arimo:wght@400;700&display=swap">
<style>
:root{
  --blue:#0a57b0;
  --blue-deep:#0a4fa3;
  --navy:#1d2238;
  --ink:#1c2333;
  --text:#5a5f6a;
  --pale:#eaf3f8;
  --white:#fff;
  --rule:#d7dbe2;
}
*{margin:0;padding:0;box-sizing:border-box}
html,body{width:1200px;height:4270px;overflow:hidden}
body{position:relative;background:var(--white);font-family:"Arimo",Arial,sans-serif;color:var(--text)}
.abs{position:absolute}
.display{font-family:"Bebas Neue",Impact,sans-serif;letter-spacing:.3px;color:var(--ink)}
.kicker{font-family:"Bebas Neue",Impact,sans-serif;color:var(--blue);font-size:17px;letter-spacing:.3px}
.title{font-family:"Bebas Neue",Impact,sans-serif;color:var(--ink);font-size:32px;letter-spacing:.4px}
.bar{height:4px;width:56px;background:var(--blue)}
.center{left:0;width:1200px;text-align:center}
.bar.centered{left:572px}
.body-text{font-size:11.5px;line-height:17px;color:var(--text)}
.btn{display:flex;align-items:center;justify-content:center;font-family:"Bebas Neue",Impact,sans-serif;font-size:16px;border-radius:20px;letter-spacing:.3px}
.btn-outline{border:2px solid var(--blue);color:var(--blue);background:var(--white)}

/* header */
.site-header{left:0;top:0;width:1200px;height:80px;background:var(--white)}
.brand{font-family:"Raleway",Arial,sans-serif;font-weight:700;color:var(--ink);line-height:1}
.brand .name{font-size:22px;letter-spacing:1.5px}
.brand .sub{font-size:10px;letter-spacing:9px;margin-top:6px}
.nav a{position:absolute;top:31px;font-family:"Bebas Neue",Impact,sans-serif;font-size:16px;color:var(--ink);text-decoration:none;letter-spacing:.3px}
.nav .active-line{position:absolute;left:532px;top:76px;width:46px;height:4px;background:var(--blue)}

/* hero */
.hero{left:0;top:80px;width:1200px;height:620px;background:linear-gradient(100deg,#1f2530 0%,#3a4250 45%,#2a3038 70%,#151a22 100%)}
.hero-brand{left:138px;top:250px;font-family:"Raleway",Arial,sans-serif;font-weight:700;font-size:43px;color:#2a8fe0;letter-spacing:.5px}
.hero-head{left:138px;top:297px;font-family:"Raleway",Arial,sans-serif;font-weight:800;font-size:30px;line-height:37px;color:var(--white)}
.hero-copy{left:138px;top:374px;width:540px;font-family:"Raleway",Arial,sans-serif;font-weight:500;font-size:14px;line-height:20px;color:var(--white)}
.btn-solid{background:var(--blue);color:var(--white)}
.btn-light{background:var(--white);color:var(--blue)}
.dot{width:14px;height:14px;border-radius:50%;top:662px}

/* services */
.services{left:0;top:1271px;width:1200px;height:694px;background:var(--pale)}
.svc h3{font-family:"Bebas Neue",Impact,sans-serif;font-size:19px;color:var(--ink);font-weight:400;letter-spacing:.3px}
.svc p{margin-top:10px;width:290px}
.svc ul{list-style:none;display:grid;grid-template-columns:144px 150px;row-gap:13px;margin-top:18px}
.svc li{font-size:10.5px;color:var(--ink);padding-left:10px;position:relative;line-height:17px}
.svc li:before{content:"";position:absolute;left:0;top:6px;width:6px;height:6px;border-radius:50%;background:var(--blue)}
.icon-badge{width:78px;height:78px;border-radius:50%;background:var(--white);display:flex;align-items:center;justify-content:center}
.icon-badge span{width:60px;height:60px;border-radius:50%;background:var(--blue);display:flex;align-items:center;justify-content:center}

/* edge */
.edge{left:0;top:1965px;width:1200px;height:509px;background:var(--blue-deep)}
.edge .kicker,.edge .title{color:var(--white)}
.edge-item{width:280px;text-align:center;color:var(--white)}
.edge-item h4{font-family:"Bebas Neue",Impact,sans-serif;font-weight:400;font-size:19px;letter-spacing:.3px}
.edge-item p{font-size:10.5px;line-height:15px;margin-top:6px}
.big-num{font-family:"Bebas Neue",Impact,sans-serif;font-size:78px;color:rgba(255,255,255,.18);line-height:1}

/* news */
.card{width:295px;height:437px;background:var(--white);box-shadow:0 4px 18px rgba(20,40,80,.12)}
.card .thumb{width:295px;height:202px}
.card .date{position:absolute;left:20px;top:228px;font-family:"Bebas Neue",Impact,sans-serif;font-size:12px;color:var(--blue)}
.card h4{position:absolute;left:20px;top:252px;font-family:"Bebas Neue",Impact,sans-serif;font-weight:400;font-size:17px;color:var(--ink)}
.card p{position:absolute;left:20px;top:282px;width:245px}
.card .btn{position:absolute;left:20px;top:381px;width:122px;height:36px}

/* contact */
.contact{left:0;top:3185px;width:1200px;height:664px;background:var(--pale)}
.find-us{left:134px;top:3261px;width:199px;height:381px;background:var(--blue-deep);color:var(--white)}
.find-us h5{font-family:"Bebas Neue",Impact,sans-serif;font-weight:400;font-size:17px}
.find-us .lbl{font-family:"Bebas Neue",Impact,sans-serif;font-size:13px}
.find-us .val{font-size:10.5px;line-height:13px;color:#cfe0f6}
.social{width:14px;height:14px;border-radius:50%;background:var(--white)}
.map{left:333px;top:3261px;width:191px;height:381px;background:linear-gradient(160deg,#efe8dc,#e4ead9 55%,#dfe7ef)}
.form-card{left:487px;top:3322px;width:577px;height:456px;background:var(--white);box-shadow:0 4px 20px rgba(20,40,80,.1)}
.field .lbl{font-family:"Bebas Neue",Impact,sans-serif;font-size:13px;color:var(--ink)}
.field .ph{font-size:10px;color:#8a8f99;margin-top:6px}
.field .line{height:1px;background:var(--rule)}

/* footer */
.site-footer{left:0;top:3849px;width:1200px;height:421px;background:var(--navy)}
.newsletter{left:340px;top:3977px;width:520px;height:41px;background:var(--white);border-radius:21px;font-size:11px;color:#9aa0aa;padding:14px 0 0 30px}
.submit{left:739px;top:3977px;width:121px;height:41px;background:var(--blue);border-radius:21px;color:var(--white)}
.foot-rule{left:134px;width:930px;height:1px;background:rgba(255,255,255,.15)}
.foot-nav a{position:absolute;top:4174px;font-family:"Bebas Neue",Impact,sans-serif;font-size:16px;color:var(--white);text-decoration:none}
.legal{top:4223px;font-size:10px;color:#6f7690}
</style>
</head>
<body>

<header class="abs site-header">
  <div class="abs brand" style="left:141px;top:20px">
    <div class="name">BRIGHTMOOR VECTOR</div>
    <div class="sub">SYSTEMS</div>
  </div>
  <nav class="nav">
    <a href="#" style="left:540px">Home</a>
    <a href="#" style="left:633px">About Us</a>
    <a href="#" style="left:750px">Our Services</a>
    <a href="#" style="left:890px">Blog</a>
    <a href="#" style="left:983px">Contact Us</a>
    <span class="active-line"></span>
  </nav>
</header>

<section class="abs hero" role="img" aria-label="Businessman with briefcase climbing a staircase toward a city skyline with rising arrows"></section>
<div class="abs hero-brand">BRIGHTMOOR</div>
<h1 class="abs hero-head">YOUR BUSINESS A GROWTH<br>AND THE FUTURE</h1>
<p class="abs hero-copy">It uses a dictionary of over 200 Latin words, combined with a handful of model sentence structures, to generate Lorem Ipsum which looks reasonable.</p>
<a class="abs btn btn-solid" style="left:138px;top:444px;width:150px;height:36px">Get Started</a>
<a class="abs btn btn-light" style="left:297px;top:444px;width:150px;height:36px">Read More</a>
<span class="abs dot" style="left:1064px;background:var(--blue)"></span>
<span class="abs dot" style="left:1087px;background:var(--white)"></span>
<span class="abs dot" style="left:1110px;background:var(--white)"></span>
<span class="abs dot" style="left:1133px;background:var(--white)"></span>

<section class="about">
  <div class="abs" role="img" aria-label="Circular blue technology ring framing a team of business people reviewing a chart" style="left:136px;top:766px;width:398px;height:398px;border-radius:50%;background:radial-gradient(circle,#e9edf2 0 34%,#ffffff 34% 38%,#1863c4 38% 62%,#ffffff 62% 64%,#0a4aa0 64%)"></div>
  <div class="abs kicker" style="left:608px;top:793px">Who We Are</div>
  <h2 class="abs title" style="left:608px;top:818px">About <span style="color:var(--blue)">Brightmoor Vector Systems</span></h2>
  <div class="abs bar" style="left:608px;top:865px;width:78px"></div>
  <p class="abs body-text" style="left:608px;top:902px;width:456px">We There are many variations of passages of Lorem Ipsum available, but the majority have suffered alteration in some form, by injected humour, or randomised words which don't look even slightly believable. If you are going to use a passage of Lorem Ipsum, you need to be sure there isn't anything embarrassing hidden in the middle of text. All the Lorem Ipsum generators on the Internet tend to repeat predefined chunks as necessary, making this the first true generator on the Internet.</p>
  <p class="abs body-text" style="left:608px;top:1024px;width:456px">It uses a dictionary of over 200 Latin words, combined with a handful of model sentence structures, to generate Lorem Ipsum which looks reasonable. The generated Lorem Ipsum is therefore always free from repetition, injected humour, or non-characteristic words etc.</p>
  <a class="abs btn btn-outline" style="left:608px;top:1127px;width:151px;height:37px">Read More</a>
</section>

<section class="abs services"></section>
<div class="abs kicker center" style="top:1321px">What We Do</div>
<h2 class="abs title center" style="top:1345px">Our Professional Services</h2>
<div class="abs bar centered" style="top:1394px"></div>

<svg class="abs" style="left:500px;top:1450px" width="200" height="450" viewBox="0 0 200 450" fill="none" stroke="#b9c9dc" stroke-dasharray="5 4" stroke-width="1.5">
  <path d="M50 34 H70 Q85 34 85 50 V440"/>
  <path d="M150 34 H130 Q115 34 115 50 V440"/>
  <path d="M50 248 H70 Q80 248 80 260 V440"/>
  <path d="M150 248 H130 Q120 248 120 260 V440"/>
  <path d="M100 60 V440"/>
</svg>

<div class="abs icon-badge" style="left:474px;top:1445px"><span><svg width="28" height="28" viewBox="0 0 28 28" fill="#fff"><rect x="4" y="5" width="20" height="13" rx="2"/><path d="M9 18 L9 24 L15 18Z"/></svg></span></div>
<div class="abs icon-badge" style="left:646px;top:1445px"><span><svg width="28" height="28" viewBox="0 0 28 28" fill="none" stroke="#fff" stroke-width="2"><circle cx="14" cy="14" r="5"/><path d="M14 3v5M14 20v5M3 14h5M20 14h5M6 6l3.5 3.5M18.5 18.5L22 22M22 6l-3.5 3.5M9.5 18.5L6 22"/></svg></span></div>
<div class="abs icon-badge" style="left:474px;top:1659px"><span><svg width="28" height="28" viewBox="0 0 28 28" fill="none" stroke="#fff" stroke-width="2"><circle cx="14" cy="14" r="10"/><path d="M4 14h20M14 4c-4 4-4 16 0 20M14 4c4 4 4 16 0 20"/></svg></span></div>
<div class="abs icon-badge" style="left:646px;top:1659px"><span><svg width="28" height="28" viewBox="0 0 28 28" fill="#fff" stroke="#fff" stroke-width="2"><rect x="10" y="3" width="8" height="7"/><rect x="3" y="19" width="8" height="7"/><rect x="17" y="19" width="8" height="7"/><path d="M14 10v5M7 19v-4h14v4" fill="none"/></svg></span></div>

<div class="abs svc" style="left:134px;top:1444px">
  <h3>Consulting</h3>
  <p class="body-text">We There are many variations of passages of Lorem Ipsum available, but the majority have suffered alteration in some form, by injected humour, or randomised words which don't look even slightly believable.</p>
  <ul><li>Enterprise -Wide</li><li>Application Modernisation</li><li>IT Management</li><li>IT Management</li><li>Cloud Computing</li><li>Cloud Computing</li></ul>
</div>
<div class="abs svc" style="left:764px;top:1444px">
  <h3>Managed IT Services</h3>
  <p class="body-text">We There are many variations of passages of Lorem Ipsum available, but the majority have suffered alteration in some form, by injected humour, or randomised words which don't look even slightly believable.</p>
  <ul><li>Security</li><li>Application Modernisation</li><li>Cloud Team</li><li>Application developemtn</li><li>Data Managemetn</li><li>Cloud Computing</li></ul>
</div>
<div class="abs svc" style="left:134px;top:1658px">
  <h3>Busines Solutions</h3>
  <p class="body-text">We There are many variations of passages of Lorem Ipsum available, but the majority have suffered alteration in some form, by injected humour, or randomised words which don't look even slightly believable.</p>
  <ul><li>Cloud Computing</li><li>Application Modernisation</li><li>User Experience</li><li>Business Outsourcing</li><li>Cloud Computing</li><li>Cloud Computing</li></ul>
</div>
<div class="abs svc" style="left:764px;top:1658px">
  <h3>Business Process Optimisation</h3>
  <p class="body-text">We There are many variations of passages of Lorem Ipsum available, but the majority have suffered alteration in some form, by injected humour, or randomised words which don't look even slightly believable.</p>
  <ul><li>Business Process</li><li>Application Modernisation</li><li>IT Management</li><li>IT Management</li><li>Cloud Computing</li><li>Cloud Computing</li></ul>
</div>

<section class="abs edge"></section>
<div class="abs" style="left:504px;top:1875px;width:188px;height:188px;border-radius:50%;border:2px solid rgba(10,87,176,.35);background:rgba(255,255,255,.06)"></div>
<div class="abs" style="left:520px;top:1891px;width:156px;height:156px;border-radius:50%;background:var(--blue-deep);border:5px solid var(--white);box-shadow:0 6px 16px rgba(0,0,0,.2)"></div>
<svg class="abs" style="left:570px;top:1908px" width="56" height="60" viewBox="0 0 56 60" fill="#fff" stroke="#fff" stroke-width="3" stroke-linecap="round">
  <path d="M28 14c-9 0-15 6-15 14 0 5 3 8 6 11 2 2 2 4 2 6h14c0-2 0-4 2-6 3-3 6-6 6-11 0-8-6-14-15-14z" stroke="none"/>
  <rect x="21" y="47" width="14" height="4" stroke="none"/><rect x="23" y="53" width="10" height="3" stroke="none"/>
  <path d="M28 2v6M8 10l4 4M48 10l-4 4M2 28h5M49 28h5" fill="none"/>
</svg>
<div class="abs display center" style="top:1985px;font-size:31px;color:var(--white)">Our Edge</div>
<svg class="abs" style="left:592px;top:2068px" width="12" height="22" viewBox="0 0 12 22" fill="none" stroke="#fff" stroke-width="1.5"><path d="M6 0v20M1 15l5 5 5-5"/></svg>
<div class="abs kicker center" style="top:2104px;color:var(--white);font-size:16px">Why Choose Us</div>
<h2 class="abs title center" style="top:2127px;color:var(--white);font-size:31px">All Business and Techch Services</h2>
<div class="abs bar centered" style="top:2178px;background:var(--white)"></div>
<svg class="abs" style="left:280px;top:2187px" width="640" height="145" viewBox="0 0 640 145" fill="none" stroke="#fff" stroke-width="1.5" stroke-dasharray="6 4">
  <path d="M310 0 V52 Q310 60 302 60 H18 Q10 60 10 68 V128"/>
  <path d="M330 0 V52 Q330 60 338 60 H622 Q630 60 630 68 V128"/>
  <path d="M320 0 V128"/>
  <circle cx="10" cy="135" r="6" fill="#fff" stroke="none"/>
  <circle cx="320" cy="135" r="6" fill="#fff" stroke="none"/>
  <circle cx="630" cy="135" r="6" fill="#fff" stroke="none"/>
</svg>
<div class="abs big-num" style="left:240px;top:2264px">1</div>
<div class="abs big-num" style="left:540px;top:2264px">2</div>
<div class="abs big-num" style="left:856px;top:2264px">3</div>
<div class="abs edge-item" style="left:150px;top:2350px"><h4>Proven Track Record</h4><p>We There are many variations of passages of Lorem Ipsum available, but the majority have suffered alteration in some form, by injected humour,</p></div>
<div class="abs edge-item" style="left:460px;top:2350px"><h4>Pioneers in the Industry</h4><p>We There are many variations of passages of Lorem Ipsum available, but the majority have suffered alteration in some form, by injected humour,</p></div>
<div class="abs edge-item" style="left:770px;top:2350px"><h4>Ensured Service Levels</h4><p>We There are many variations of passages of Lorem Ipsum available, but the majority have suffered alteration in some form, by injected humour,</p></div>

<section class="news">
  <div class="abs kicker center" style="top:2548px">News and Blogs</div>
  <h2 class="abs title center" style="top:2572px">Our Insights and Views</h2>
  <div class="abs bar centered" style="top:2620px"></div>

  <article class="abs card" style="left:134px;top:2673px">
    <div class="thumb" role="img" aria-label="Blue circuit style banner with the word technology" style="background:linear-gradient(135deg,#0b3f94,#1565c8)"></div>
    <div class="date">30 June 2021</div><h4>Where Can I Get Some?</h4>
    <p class="body-text">We There are many variations of passages of Lorem Ipsum available, but the majority have suffered alteration in some form, by injected humour, or randomised words which don't look even slightly believable.</p>
    <a class="btn btn-outline">Read More</a>
  </article>
  <article class="abs card" style="left:451px;top:2673px">
    <div class="thumb" role="img" aria-label="Business team gathered around a laptop in a bright office" style="background:linear-gradient(135deg,#cfd6dd,#8d97a3 60%,#4d5663)"></div>
    <div class="date">30 January 2021</div><h4>Where Does It Come From?</h4>
    <p class="body-text">We There are many variations of passages of Lorem Ipsum available, but the majority have suffered alteration in some form, by injected humour, or randomised words which don't look even slightly believable.</p>
    <a class="btn btn-outline">Read More</a>
  </article>
  <article class="abs card" style="left:769px;top:2673px">
    <div class="thumb" role="img" aria-label="Hands over a desk with a business plan sketch and charts" style="background:linear-gradient(135deg,#e8edf3,#b3c4d8 55%,#4a6385)"></div>
    <div class="date">30 December 2021</div><h4>Why Do We Use It?</h4>
    <p class="body-text">We There are many variations of passages of Lorem Ipsum available, but the majority have suffered alteration in some form, by injected humour, or randomised words which don't look even slightly believable.</p>
    <a class="btn btn-outline">Read More</a>
  </article>
</section>

<section class="abs contact"></section>
<div class="abs find-us">
  <h5 class="abs" style="left:22px;top:38px">Find Us</h5>
  <div class="abs" style="left:22px;top:80px"><div class="lbl">Address</div><div class="val">Location Town, City name<br>Country</div></div>
  <div class="abs" style="left:22px;top:142px"><div class="lbl">Phone</div><div class="val">123-456-7895</div></div>
  <div class="abs" style="left:22px;top:194px"><div class="lbl">Email</div><div class="val">info@brightmoorvector.com</div></div>
  <div class="abs lbl" style="left:22px;top:298px">Follow Us</div>
  <span class="abs social" style="left:22px;top:330px"></span>
  <span class="abs social" style="left:52px;top:330px"></span>
  <span class="abs social" style="left:82px;top:330px"></span>
  <span class="abs social" style="left:112px;top:330px"></span>
</div>
<div class="abs map" role="img" aria-label="Embedded road map showing the office location"></div>
<svg class="abs" style="left:438px;top:3438px" width="20" height="28" viewBox="0 0 20 28"><path d="M10 0C4 0 0 4 0 10c0 7 10 18 10 18s10-11 10-18C20 4 16 0 10 0z" fill="#e53935"/><circle cx="10" cy="10" r="4" fill="#8e1c1a"/></svg>

<div class="abs form-card">
  <div class="abs kicker" style="left:37px;top:60px">Contact Us</div>
  <h2 class="abs title" style="left:37px;top:83px;font-size:30px">Get in Touch With Us</h2>
  <div class="abs bar" style="left:37px;top:132px"></div>
  <div class="abs field" style="left:37px;top:172px;width:240px"><div class="lbl">First Name</div><div class="ph">&nbsp;</div><div class="line" style="margin-top:9px"></div></div>
  <div class="abs field" style="left:300px;top:172px;width:240px"><div class="lbl">Lastt Name</div><div class="ph">Doe</div><div class="line" style="margin-top:9px"></div></div>
  <div class="abs field" style="left:37px;top:253px;width:240px"><div class="lbl">Email Address</div><div class="ph">johndoe@clientemailid.com</div><div class="line" style="margin-top:9px"></div></div>
  <div class="abs field" style="left:300px;top:253px;width:240px"><div class="lbl">Phone No.</div><div class="ph">123-456-7895</div><div class="line" style="margin-top:9px"></div></div>
  <div class="abs field" style="left:25px;top:332px;width:515px"><div class="lbl">Message</div><div class="ph" style="margin-top:14px">Let's talk</div><div class="line" style="margin-top:26px"></div></div>
</div>

<footer class="abs site-footer"></footer>
<h2 class="abs title center" style="top:3919px;color:var(--white);font-size:32px">Our News Letter</h2>
<div class="abs newsletter">johndoe@clientemailid.com</div>
<div class="abs btn submit">Submit</div>
<div class="abs brand center" style="top:4075px;color:var(--white)">
  <div class="name">BRIGHTMOOR VECTOR</div>
  <div class="sub">SYSTEMS</div>
</div>
<div class="abs foot-rule" style="top:4151px"></div>
<nav class="foot-nav">
  <a href="#" style="left:343px">Home</a>
  <a href="#" style="left:438px">About Us</a>
  <a href="#" style="left:555px">Our Services</a>
  <a href="#" style="left:695px">Blog</a>
  <a href="#" style="left:788px">Contact Us</a>
</nav>
<div class="abs foot-rule" style="top:4205px"></div>
<div class="abs legal" style="left:134px">COPYRIGHT © 2021 BRIGHTMOOR VECTOR SYSTEMS</div>
<div class="abs legal" style="left:842px">PRIVACY POLICY &nbsp;|&nbsp; TERMS OF SERVICES</div>

</body>
</html>
```